Fun Dry Cleaners Business Flyer

We need a 5.5x8.5 business flyer designed for a new dry cleaners based in Texas called "Copperleaf Dry Cleaners". The flyer needs to be 2 sided (no fold) with the front side containing advertising information (slogan, hours of operation, address, etc...) along with the attached logo. The back will need to include the services and prices. The dry cleaners is a sports themed dry cleaners and we occasionally give away free game tickets (pro football, basketball, baseball, college sports tickets and memorabilia also). The design should be fun like the logo but also professional and appealing. We have no particular restrictions on the colors to be used.

The following should be included

Address - 418 N Bramble Ln
Waco, TX, 76704

Two Day Service
Dry Cleaning
Shirts - $1.50
Complete Suits - $9.99
Blouse - $3.00
Jeans/Pants - $4.00
Jackets - $5.00
Alterations
and More...

Hours of Operation: Monday - Friday 7 am - 6pm
Saturday 10am - 4pm
Sunday - Closed

Target Market(s)

Adults 21 and over
Business Professionals
People who go to Church etc...
Students

Industry/Entity Type

Dry Cleaner

Font styles to use
Serif
Sans Serif
Decorative

Colors

Designer to choose colors to be used in the design.

Requirements
Must have
• Logo should be incorporated within the flyer and naturally flow with the design
• The following should be included
• Address - 418 N Bramble Ln
• Waco, TX, 76704
• Two Day Service
• Dry Cleaning
• Shirts $1.25
• Complete Suits $9.99
• Jeans $3.99
• Slacks $3.99
• Sport Coats $3..99
• Blouses $2.99
• Pullovers $3.49
• Dresses $9.99
• Alterations
• and More...
• Hours of Operation: Monday - Friday 7 am - 6pm
• Saturday 10am - 4pm
• Sunday - Closed
• Phone Number - 254-618-5207
Nice to have
• Fun Design but professional, nice color scheme and flow, address should be visible and not hidden on the flyer

```html
<!DOCTYPE html>
<html lang="en">
<head>
<meta charset="utf-8">
<title>Copperleaf Dry Cleaners – Flyer</title>
<link rel="stylesheet" href="https://fonts.googleapis.com/css2?family=Roboto:ital,wght@0,400;0,700;0,900;1,700;1,900&family=Yellowtail&display=swap">
<style>
  :root{
    --stage:#2b1d16;
    --green-dark:#1c8a31;
    --green:#2ea63b;
    --green-lime:#7cc242;
    --lime-box:#8cc63f;
    --sky-top:#3f9be0;
    --sky-bottom:#cfe9f7;
    --navy:#16337a;
    --phone-edge:#8fd3ff;
    --ink:#000;
    --white:#fff;
  }
  *{box-sizing:border-box;margin:0;padding:0}
  html,body{width:1200px;height:1200px;overflow:hidden;background:var(--stage)}
  .canvas{position:relative;width:1200px;height:1200px}
  .flyer{position:absolute;top:182px;width:540px;height:835px;overflow:hidden;font-family:"Roboto",sans-serif;color:var(--white)}
  .flyer--prices{left:40px;background:radial-gradient(circle at 113px 104px,#d7f06a 0,#5cc04a 90px,var(--green) 200px,var(--green-dark) 560px)}
  .flyer--front{left:620px;background:linear-gradient(180deg,var(--sky-top) 0%,#7cc0ec 45%,var(--sky-bottom) 100%)}

  .brand{position:absolute;display:flex;flex-direction:column;align-items:center;gap:8px;text-align:center}
  .brand__dot{width:34px;height:34px;border-radius:50%;background:var(--white)}
  .brand__name{font-weight:900;font-size:22px;line-height:1.1;color:var(--white)}
  .flyer--prices .brand{left:18px;top:58px;width:190px}
  .flyer--front .brand{left:120px;top:50px;width:300px}
  .flyer--front .brand__name{font-size:30px}

  .services{position:absolute;left:230px;top:44px;width:290px}
  .services__title{font-weight:900;font-style:italic;font-size:30px;line-height:38px}
  .price-list{list-style:none;margin-top:6px}
  .price-list li{display:flex;justify-content:space-between;align-items:center;height:33px;font-size:20px}
  .price{width:82px;height:25px;background:var(--lime-box);font-size:20px;line-height:25px;padding-left:8px}
  .services__more{font-size:20px;margin-top:2px}
  .services__more em{font-weight:900;font-size:17px}

  .photo{position:absolute}
  .photo--shop{left:0;top:300px;width:540px;height:470px;
    background:linear-gradient(180deg,rgba(46,166,59,1) 0%,rgba(200,210,215,.9) 22%,#b9bfc6 45%,#9b6e6e 70%,#3b4a72 100%)}
  .photo--stack{left:110px;top:270px;width:430px;height:500px;
    background:linear-gradient(180deg,rgba(240,244,248,0) 0%,#eef1f4 12%,#b7a897 28%,#2f8fd0 42%,#e2338a 58%,#f26a2a 70%,#9cc74a 80%,#e85aa0 92%,#5bc6d8 100%)}

  .slogan{position:absolute;left:0;width:540px;height:80px;line-height:80px;text-align:center;font-family:"Yellowtail",cursive;font-size:60px;color:var(--white);-webkit-text-stroke:1.5px var(--green);white-space:nowrap;transform:rotate(-13deg);transform-origin:50% 50%}
  .flyer--prices .slogan{top:390px}
  .flyer--front .slogan{top:200px}

  .arc{position:absolute;left:0;top:0;width:540px;height:835px}
  .contact{position:absolute;left:0;top:618px;width:540px;text-align:center}
  .contact__cta{font-weight:900;font-style:italic;font-size:31px;color:var(--navy);-webkit-text-stroke:1px var(--phone-edge)}
  .contact__phone{font-weight:900;font-style:italic;font-size:36px;letter-spacing:2px;line-height:40px;color:var(--navy);-webkit-text-stroke:1.5px var(--phone-edge)}
  .contact__hours{font-size:17.5px;line-height:23px;margin-top:4px}
  .contact__hours strong{font-style:italic;font-weight:900}
  .address{position:absolute;left:0;top:763px;width:540px;height:72px;background:var(--ink);text-align:center;font-weight:700;font-size:15.5px;padding-top:18px}
</style>
</head>
<body>
<main class="canvas">

  <section class="flyer flyer--prices" aria-label="Flyer back: services and prices">
    <div class="photo photo--shop" role="img" aria-label="Photo of a dry cleaning shop with garments on racks and an attendant holding a bagged shirt"></div>

    <div class="brand">
      <span class="brand__dot"></span>
      <span class="brand__name">Copperleaf Dry Cleaners</span>
    </div>

    <div class="services">
      <h2 class="services__title">Two Day Service<br>Dry Cleaning</h2>
      <ul class="price-list">
        <li>Shirts <span class="price">$1.50</span></li>
        <li>Complete Suits <span class="price">$9.99</span></li>
        <li>Blouse <span class="price">$3.00</span></li>
        <li>Jeans/Pants <span class="price">$4.00</span></li>
        <li>Jackets <span class="price">$5.00</span></li>
      </ul>
      <p class="services__more">Alterations <em>and More...</em></p>
    </div>

    <p class="slogan">Always Sparkling</p>

    <svg class="arc" viewBox="0 0 540 835" aria-hidden="true">
      <path d="M0,745 Q270,490 540,715 L540,763 L0,763 Z" fill="var(--green-lime)"/>
    </svg>
    <div class="contact">
      <p class="contact__cta">Call Us Now</p>
      <p class="contact__phone">254-618-5207</p>
      <p class="contact__hours">Hours of Operation: Monday - Friday 7 am - 6pm<br>Saturday 10am - 4pm&nbsp; <strong>Sunday - Closed</strong></p>
    </div>
    <p class="address">Address - 418 N Bramble Ln&nbsp; Waco, TX, 76704</p>
  </section>

  <section class="flyer flyer--front" aria-label="Flyer front">
    <div class="photo photo--stack" role="img" aria-label="Photo of a tall stack of neatly folded colourful clothes and towels"></div>

    <div class="brand">
      <span class="brand__dot"></span>
      <span class="brand__name">Copperleaf Dry Cleaners</span>
    </div>

    <p class="slogan">Always Sparkling</p>

    <svg class="arc" viewBox="0 0 540 835" aria-hidden="true">
      <path d="M0,745 Q270,490 540,715 L540,763 L0,763 Z" fill="var(--green-lime)"/>
    </svg>
    <div class="contact">
      <p class="contact__cta">Call Us Now</p>
      <p class="contact__phone">254-618-5207</p>
      <p class="contact__hours">Hours of Operation: Monday - Friday 7 am - 6pm<br>Saturday 10am - 4pm&nbsp; <strong>Sunday - Closed</strong></p>
    </div>
    <p class="address">Address - 418 N Bramble Ln&nbsp; Waco, TX, 76704</p>
  </section>

</main>
</body>
</html>
```